Bref créative
BrightPath Fuel
Eye Catching Card & Letterhead Design
Professional
Marcus Torres
CEO
4183 HAWTHORNE AVE
SUITE 310
SARASOTA FL 34519
mtorres@brightpathfuel.example
www.brightpathfuel.example
use the WELL portion of the logo and list the twitter site (@brightpathfuel)

```html
<!DOCTYPE html>
<html lang="en">
<head>
<meta charset="utf-8">
<title>BrightPath Fuel – Business Cards</title>
<link rel="stylesheet" href="https://fonts.googleapis.com/css2?family=Montserrat:wght@600;700&family=Open+Sans+Condensed:wght@300;700&family=Open+Sans:wght@400;600;700&display=swap">
<style>
  :root {
    --bg: #e9e6e1;
    --card-white: #ffffff;
    --green: #8cbf3f;
    --green-light: #a9d15a;
    --green-dark: #79ad2f;
    --ink: #3a3a3a;
    --ink-soft: #5a5a5a;
    --black: #111111;
    --grey-line: #d8d8d8;
  }
  * { box-sizing: border-box; margin: 0; padding: 0; }
  html, body { width: 1200px; height: 775px; overflow: hidden; }
  body {
    background: var(--bg);
    position: relative;
    font-family: "Open Sans", Arial, sans-serif;
    color: var(--ink);
  }
  .card {
    position: absolute;
    width: 480px;
    height: 288px;
    overflow: hidden;
    box-shadow: 0 4px 10px rgba(0,0,0,.18);
  }
  .card--front { left: 84px; top: 72px; background: var(--card-white); }
  .card--back-green { left: 616px; top: 72px; background: radial-gradient(ellipse at 50% 45%, var(--green-light), var(--green-dark)); }
  .card--back-white { left: 360px; top: 432px; background: var(--card-white); }

  .swoosh { position: absolute; inset: 0; width: 480px; height: 288px; }

  .brand {
    position: absolute; left: 0; right: 0;
    text-align: center;
    font-family: "Montserrat", Arial, sans-serif;
    font-weight: 700;
    letter-spacing: -0.5px;
    text-transform: uppercase;
  }
  .brand-dot {
    position: absolute; left: 50%;
    border-radius: 50%;
    transform: translateX(-50%);
  }

  /* front */
  .card--front .brand-dot { top: 22px; width: 34px; height: 34px; background: var(--green); }
  .card--front .brand { top: 62px; font-size: 35px; color: var(--ink); }
  .person {
    position: absolute; left: 0; right: 0; top: 118px;
    text-align: center; font-weight: 700; font-size: 19px; color: var(--ink);
  }
  .person .role { font-weight: 400; font-size: 15px; color: var(--ink-soft); }
  .contact {
    position: absolute; left: 0; right: 0;
    text-align: center;
    font-family: "Open Sans Condensed", Arial Narrow, sans-serif;
    font-weight: 300; font-size: 12.5px; color: var(--ink);
    white-space: nowrap;
  }
  .contact--address { top: 160px; }
  .contact--lines { top: 178px; }
  .contact--web { top: 196px; }
  .icon {
    display: inline-block; width: 9px; height: 9px; border-radius: 50%;
    background: var(--green); vertical-align: -1px; margin: 0 3px 0 8px;
  }
  .contact--web .icon { margin-left: 0; }

  /* green back */
  .card--back-green .brand-dot { top: 58px; width: 44px; height: 44px; background: #ffffff; }
  .card--back-green .brand { top: 112px; font-size: 42px; color: #ffffff; }
  .social {
    position: absolute; left: 0; right: 0;
    text-align: center; font-size: 11px; font-weight: 600;
  }
  .social-square {
    display: inline-block; width: 11px; height: 11px; border-radius: 2px;
    vertical-align: -1px; margin-right: 5px;
  }
  .web-bold {
    position: absolute; left: 0; right: 0;
    text-align: center; font-weight: 700; font-size: 11px; letter-spacing: 2.5px;
  }
  .card--back-green .social { top: 200px; color: #ffffff; }
  .card--back-green .social-square { background: #ffffff; }
  .card--back-green .web-bold { top: 230px; color: #ffffff; }

  /* white back */
  .card--back-white .brand-dot { top: 60px; width: 60px; height: 60px; background: var(--green); }
  .card--back-white .brand { top: 132px; font-size: 30px; color: var(--ink); }
  .card--back-white .social { top: 205px; color: var(--ink); }
  .card--back-white .social-square { background: var(--ink); }
  .card--back-white .web-bold { top: 230px; color: var(--ink); }
</style>
</head>
<body>

<section class="card card--front" aria-label="Business card front">
  <svg class="swoosh" viewBox="0 0 480 288" aria-hidden="true">
    <path d="M0,182 C110,228 230,262 330,288 L0,288 Z" fill="var(--black)"/>
    <path d="M0,206 C160,262 330,258 480,160 L480,174 C330,272 160,280 0,222 Z" fill="var(--green)"/>
    <path d="M300,288 C380,270 440,240 480,205 L480,212 C440,248 390,276 330,288 Z" fill="var(--grey-line)"/>
  </svg>
  <span class="brand-dot"></span>
  <div class="brand">BrightPath Fuel</div>
  <div class="person">Marcus Torres <span class="role">/ CEO</span></div>
  <div class="contact contact--address">4183 HAWTHORNE AVE SUITE 310 SARASOTA FL 34519</div>
  <div class="contact contact--lines"><span class="icon"></span>407.555.0182 <span class="icon"></span>mtorres@brightpathfuel.example</div>
  <div class="contact contact--web"><span class="icon"></span>www.brightpathfuel.example</div>
</section>

<section class="card card--back-green" aria-label="Business card back, green">
  <span class="brand-dot"></span>
  <div class="brand">BrightPath Fuel</div>
  <div class="social"><span class="social-square"></span>@brightpathfuel</div>
  <div class="web-bold">www.brightpathfuel.example</div>
</section>

<section class="card card--back-white" aria-label="Business card back, white">
  <span class="brand-dot"></span>
  <div class="brand">BrightPath Fuel</div>
  <div class="social"><span class="social-square"></span>@brightpathfuel</div>
  <div class="web-bold">www.brightpathfuel.example</div>
</section>

</body>
</html>
```